3 Sympathy Cards for Veterinary Hospital

Hi. Brookvale Pet Hospital is a Veterinary Hospital in Australia. We need sympathy cards to send to grieving clients after the loss of their beloved pets.
I have attached the old designs, but we have rebranded and need something to suit our new image.

The cards should have a nice message and appeal to every owner.
They need to match our current branding, but the cards are for the clients, not to advertise us, so not too much branding.
The current cards are attached and they are good because they show a variety of animals so clients might identify with one of them.
I have attached a brown to green gradient that we use on some designs, you don't have to use it, but consider it.
I have attached a logo on background used in some of our new designs, consider using it.
I have attached a font that we use for most new branding.

Target Market(s)

Women 25 to 44

Industry/Entity Type

Veterinary

Font styles to use
Sans Serif
Script

Colors
fac994
cadf82

Requirements
Must have
• IMPORTANT - 3 different designs for the different types of pets.
• 1. Dog.
• 2. Cat.
• 3. Everything else (Rabbits, lizards, ferrets, chickens, birds, mice, rats, snakes)
Nice to have
• Caring and compassionate message.
Should not have
• Too much branding.

```html
<!DOCTYPE html>
<html lang="en">
<head>
<meta charset="utf-8">
<title>Brookvale Pet Hospital – Sympathy Cards</title>
<link href="https://fonts.googleapis.com/css2?family=Italianno&family=Montserrat:wght@500;600&display=swap" rel="stylesheet">
<style>
  :root {
    --green: #cadf82;
    --orange: #fac994;
    --cream: #f6efd9;
    --ink: #4a2e1e;
    --heart: #d7262b;
    --white: #ffffff;
    --script: "Italianno", cursive;
    --sans: "Montserrat", sans-serif;
  }
  * { margin: 0; padding: 0; box-sizing: border-box; }
  html, body { width: 1200px; height: 848px; overflow: hidden; background: var(--white); }
  .sheet { position: relative; width: 1200px; height: 848px; }

  .card { position: absolute; top: 133px; width: 355px; height: 547px; overflow: hidden; background: var(--white); }
  .card--cat { left: 37px; }
  .card--dog { left: 418px; }
  .card--other { left: 791px; }

  .fold-band { position: absolute; left: 0; top: 0; width: 100%; height: 17px; }
  .face { position: absolute; left: 0; top: 24px; width: 100%; height: 523px; }
  .block { position: absolute; }
  .green { background: var(--green); }
  .orange { background: var(--orange); }

  .swoosh { position: absolute; left: 0; top: 0; }

  .back-credit {
    position: absolute; top: 34px; width: 200px; text-align: center;
    font-family: var(--sans); font-size: 5px; line-height: 8px; color: var(--ink);
    transform: rotate(180deg);
  }
  .brand-tile {
    position: absolute; top: 53px; width: 124px; height: 107px;
    background: var(--cream); opacity: .92;
    display: flex; align-items: center; justify-content: center; text-align: center;
  }
  .brand-name {
    transform: rotate(180deg);
    font-family: var(--sans); font-weight: 600; font-size: 11px; line-height: 14px;
    letter-spacing: .5px; color: var(--ink); text-transform: uppercase;
  }

  .photo { position: absolute; box-shadow: 1px 2px 4px rgba(0,0,0,.35); }
  .photo--grid { box-shadow: none; }

  .message {
    position: absolute; font-family: var(--script); color: var(--ink);
    white-space: nowrap; line-height: 1;
  }
  .message-line { display: flex; align-items: center; gap: 4px; }
  .heart { width: 22px; height: 19px; flex: none; }
  .heart--small { width: 18px; height: 16px; }
</style>
</head>
<body>
<div class="sheet">

  <!-- Cat card -->
  <section class="card card--cat" aria-label="Cat sympathy card">
    <div class="fold-band green"></div>
    <div class="face green">
      <div class="block orange" style="left:110px; top:247px; width:245px; height:276px;"></div>
      <svg class="swoosh" width="355" height="523" viewBox="0 0 355 523">
        <path d="M0 523 C120 440 250 380 355 247 L355 523 Z" fill="#ffffff" opacity=".35"/>
      </svg>
    </div>
    <p class="back-credit" style="left:100px;">Copyright 2017 Sample Stationery Supplies<br>PO Box 120, Brookvale 2100 Ph: 1800 000 000</p>
    <div class="brand-tile" style="left:131px;"><span class="brand-name">Brookvale<br>Pet Hospital</span></div>

    <div class="photo" role="img" aria-label="Photo of a grey tabby cat lying down" style="left:0; top:288px; width:103px; height:76px; background:linear-gradient(135deg,#cfcfc8,#8f8a80);"></div>
    <div class="photo" role="img" aria-label="Photo of a ginger kitten peeking over a ledge" style="left:26px; top:372px; width:123px; height:78px; background:linear-gradient(135deg,#e9c58e,#b47c45);"></div>
    <div class="photo" role="img" aria-label="Photo of a silver tabby cat resting" style="left:0; top:463px; width:103px; height:73px; background:linear-gradient(135deg,#e6e8ee,#a9acb2);"></div>

    <p class="message" style="right:20px; top:312px; font-size:31px;">You remember always</p>
    <div class="message message-line" style="right:14px; top:340px; font-size:31px;">
      <svg class="heart" viewBox="0 0 22 19"><path d="M11 19 C4 13 0 9 0 5 C0 2 2.5 0 5.5 0 C8 0 10 1.5 11 3.5 C12 1.5 14 0 16.5 0 C19.5 0 22 2 22 5 C22 9 18 13 11 19 Z" fill="var(--heart)"/></svg>
      <span>make us smile...</span>
    </div>
  </section>

  <!-- Dog card -->
  <section class="card card--dog" aria-label="Dog sympathy card">
    <div class="fold-band" style="background:linear-gradient(90deg,var(--orange) 0 134px,var(--green) 134px);"></div>
    <div class="face" style="background:linear-gradient(90deg,var(--orange) 0 134px,var(--green) 134px);"></div>
    <p class="back-credit" style="left:145px;">Copyright 2017 Sample Stationery Supplies<br>PO Box 120, Brookvale 2100 Ph: 1800 000 000</p>
    <div class="brand-tile" style="left:177px;"><span class="brand-name">Brookvale<br>Pet Hospital</span></div>

    <div class="photo" role="img" aria-label="Photo of a spaniel resting its head on a log" style="left:0; top:313px; width:81px; height:95px; background:linear-gradient(135deg,#d9a468,#8c5a2e);"></div>
    <div class="photo" role="img" aria-label="Photo of a black puppy sitting between boots" style="left:97px; top:274px; width:103px; height:135px; background:linear-gradient(160deg,#5d6a80,#1d1b1c);"></div>
    <div class="photo" role="img" aria-label="Photo of a white dog with a toddler" style="left:218px; top:289px; width:135px; height:127px; background:linear-gradient(135deg,#9fb07a,#ece6da);"></div>

    <p class="message" style="right:28px; top:452px; font-size:22px;">One day I need a helping hand, and I got a paw.</p>
    <div class="message message-line" style="right:6px; top:474px; font-size:22px;">
      <svg class="heart heart--small" viewBox="0 0 22 19"><path d="M11 19 C4 13 0 9 0 5 C0 2 2.5 0 5.5 0 C8 0 10 1.5 11 3.5 C12 1.5 14 0 16.5 0 C19.5 0 22 2 22 5 C22 9 18 13 11 19 Z" fill="var(--heart)"/></svg>
      <span>I'll always remember you.</span>
    </div>
  </section>

  <!-- Other pets card -->
  <section class="card card--other" aria-label="Other pets sympathy card">
    <div class="fold-band" style="background:linear-gradient(90deg,var(--orange) 0 244px,var(--green) 244px);"></div>
    <div class="face" style="background:linear-gradient(90deg,var(--orange) 0 244px,var(--green) 244px);">
      <svg class="swoosh" width="355" height="523" viewBox="0 0 355 523">
        <path d="M0 385 L0 250 L355 250 L355 270 C280 300 150 360 0 385 Z" fill="#ffffff" opacity=".3"/>
      </svg>
    </div>
    <p class="back-credit" style="left:80px;">Copyright 2017 Sample Stationery Supplies<br>PO Box 120, Brookvale 2100 Ph: 1800 000 000</p>
    <div class="brand-tile" style="left:102px;"><span class="brand-name">Brookvale<br>Pet Hospital</span></div>

    <div class="message message-line" style="left:38px; top:334px; font-size:22px;">
      <svg class="heart heart--small" viewBox="0 0 22 19"><path d="M11 19 C4 13 0 9 0 5 C0 2 2.5 0 5.5 0 C8 0 10 1.5 11 3.5 C12 1.5 14 0 16.5 0 C19.5 0 22 2 22 5 C22 9 18 13 11 19 Z" fill="var(--heart)"/></svg>
      <span>A pet leaves footprints forever in your heart</span>
    </div>

    <div class="photo photo--grid" role="img" aria-label="Photo of a rabbit with ducklings" style="left:0; top:409px; width:107px; height:57px; background:linear-gradient(135deg,#a9b86a,#e8dcb8);"></div>
    <div class="photo photo--grid" role="img" aria-label="Photo of a ferret lying on a blanket" style="left:107px; top:409px; width:128px; height:57px; background:linear-gradient(135deg,#8a8f95,#d8d2c6);"></div>
    <div class="photo photo--grid" role="img" aria-label="Photo of a pet rat" style="left:235px; top:409px; width:120px; height:57px; background:linear-gradient(135deg,#6b3b2a,#2d1a14);"></div>
    <div class="photo photo--grid" role="img" aria-label="Photo of a turtle" style="left:0; top:466px; width:107px; height:81px; background:linear-gradient(135deg,#6a5a1e,#2c2a16);"></div>
    <div class="photo photo--grid" role="img" aria-label="Photo of a lizard on a hand" style="left:107px; top:466px; width:128px; height:81px; background:linear-gradient(135deg,#d9a070,#8a6a40);"></div>
    <div class="photo photo--grid" role="img" aria-label="Photo of a turtle on a log" style="left:235px; top:466px; width:120px; height:81px; background:linear-gradient(135deg,#a8b4a0,#5a5a3c);"></div>
  </section>

</div>
</body>
</html>
```